VornaDerm/The experts in permanent hairremoval

Our Brand is VornaDerm and we are specialized on permantent hair removal for the body for men and woman. VornaDerm is working as a Franchise chain.
The brand should be positioned as lifestyle brand but with a medical background. People should trust in us. We take care about their body. This need to be communicated 100%.
Our system is inexpensive but we don't want to show that we are cheap. So we want to communicate that permanent hair removal is a real lifestyle product but affordable.
We already created a logo that you can see the style and colour we prefer.

Target Market(s)

Europe beginning (especially german spoken markets), Middle East, Africa

Industry/Entity Type

Hair Removal

Number of Pages Required

5+ page

Font styles to use
Serif
Other font styles liked:
• Trajan Pro

Requirements
Nice to have
• We are very open for new ideas

```html
<!DOCTYPE html>
<html lang="en">
<head>
<meta charset="utf-8">
<title>VornaDerm – Permanent Hair Removal</title>
<link rel="stylesheet" href="https://fonts.googleapis.com/css2?family=Montserrat:wght@500;600;700&family=Questrial&display=swap">
<style>
  :root {
    --sky: #79c4ec;
    --sky-deep: #5aafe0;
    --brand-blue: #3a9fdb;
    --nav-blue: #5fb4e4;
    --white: #ffffff;
    --paper: #f1f1f1;
    --ink: #111111;
    --numeral: #a9d7f2;
    --shadow: rgba(0, 0, 0, 0.35);
    --skin: #e9c8ab;
    --skin-light: #f3e2d2;
    --towel: #f09a3c;
  }
  * { box-sizing: border-box; margin: 0; padding: 0; }
  html, body { width: 1200px; height: 2894px; overflow: hidden; background: var(--white); }
  body { position: relative; font-family: "Questrial", sans-serif; color: var(--ink); }
  .abs { position: absolute; }
  .front { z-index: 2; }

  /* header */
  .brand { left: 139px; top: 44px; display: flex; align-items: center; gap: 10px; }
  .brand-mark { width: 14px; height: 14px; border-radius: 50%; background: var(--brand-blue); }
  .brand-name { font-family: "Questrial", sans-serif; font-size: 38px; color: var(--brand-blue); letter-spacing: 0.5px; }
  .brand-tagline { left: 163px; top: 97px; font-size: 8px; letter-spacing: 1px; color: #6a7f8e; text-transform: uppercase; }
  .main-nav { top: 59px; left: 0; width: 1200px; height: 14px; }
  .main-nav a { position: absolute; font-size: 12px; color: var(--nav-blue); text-decoration: none; text-transform: uppercase; letter-spacing: 0.5px; }

  /* hero */
  .hero-photo { left: 470px; top: 193px; width: 587px; height: 395px; background: radial-gradient(ellipse at 50% 75%, var(--skin) 0%, var(--skin-light) 45%, var(--white) 75%); }
  .hero-lead { left: 139px; top: 212px; width: 330px; font-size: 21px; line-height: 28px; color: var(--brand-blue); }
  .hero-cta { left: 139px; top: 408px; font-family: "Montserrat", sans-serif; font-weight: 600; font-size: 15px; color: var(--brand-blue); display: flex; align-items: center; gap: 12px; }

  /* about panel */
  .about-panel { left: 139px; top: 610px; width: 914px; height: 1890px; background: var(--sky); box-shadow: 10px 10px 6px var(--shadow); }
  .section-title { font-family: "Montserrat", sans-serif; font-weight: 700; color: var(--white); font-size: 28px; text-align: center; width: 914px; left: 139px; }
  .about-title { top: 630px; }
  .new-title { top: 1556px; font-weight: 600; }

  .feature-card { box-shadow: 6px 6px 6px var(--shadow); }
  .card-method { left: 0; top: 716px; width: 548px; height: 349px; background: var(--sky-deep); }
  .card-zones { left: 0; top: 1140px; width: 548px; height: 351px; background: var(--white); }
  .card-shop { left: 648px; top: 2010px; width: 552px; height: 351px; background: var(--paper); }

  .photo-method { left: 235px; top: 743px; width: 282px; height: 295px; background: linear-gradient(160deg, var(--skin-light), var(--skin) 60%, #f4f4f4); }
  .photo-zones { left: 190px; top: 1155px; width: 340px; height: 320px; background: radial-gradient(ellipse at 40% 45%, var(--skin) 0%, var(--skin-light) 40%, var(--white) 72%); }
  .photo-devices { left: 648px; top: 1688px; width: 317px; height: 179px; background: linear-gradient(90deg, #f4f4f4, #5a5a5a 30%, #f4f4f4 55%, #333 75%, #f4f4f4); }
  .photo-device-pink { left: 685px; top: 2045px; width: 280px; height: 290px; background: radial-gradient(ellipse at 50% 50%, #d9338f 0%, #f0f0f0 35%, var(--paper) 70%); }

  .numeral { font-family: "Montserrat", sans-serif; font-weight: 500; font-size: 68px; color: var(--numeral); }
  .num-01 { left: 96px; top: 770px; }
  .num-02 { left: 1018px; top: 2037px; }
  .num-rule { width: 3px; background: var(--white); }
  .rule-01 { left: 132px; top: 842px; height: 64px; }
  .rule-02 { left: 1054px; top: 2112px; height: 84px; background: var(--numeral); width: 2px; }
  .vertical-label { font-size: 9px; color: var(--white); transform: rotate(-90deg); transform-origin: left top; white-space: nowrap; }
  .vl-01 { left: 128px; top: 1040px; }
  .vl-02 { left: 1050px; top: 2250px; color: var(--numeral); }

  .feature-text { color: var(--white); width: 290px; }
  .feature-text h3 { font-family: "Montserrat", sans-serif; font-weight: 600; font-size: 28px; line-height: 32px; }
  .feature-text .sub { font-family: "Montserrat", sans-serif; font-weight: 700; font-size: 9px; margin-top: 2px; }
  .feature-text .dash { width: 40px; height: 5px; background: var(--white); margin: 34px 0 34px; }
  .feature-text p { font-family: "Montserrat", sans-serif; font-weight: 700; font-size: 9.5px; line-height: 21px; }
  .feature-text .more { margin-top: 24px; font-family: "Montserrat", sans-serif; font-weight: 700; font-size: 10px; display: flex; align-items: center; gap: 10px; text-transform: uppercase; }
  .text-method { left: 679px; top: 803px; }
  .text-zones { left: 679px; top: 1230px; }
  .text-shop { left: 278px; top: 2100px; }

  /* news band */
  .news-band { left: 0; top: 1659px; width: 1200px; height: 239px; background: var(--sky-deep); box-shadow: 0 6px 6px var(--shadow); }
  .news-copy { left: 244px; top: 1686px; width: 290px; color: var(--white); text-align: center; font-family: "Montserrat", sans-serif; font-weight: 700; font-size: 9.5px; line-height: 21px; }
  .news-copy p + p { margin-top: 22px; }
  .slider-dots { left: 532px; top: 1925px; display: flex; gap: 8px; }
  .slider-dots span { width: 40px; height: 5px; background: #a9d7f2; }
  .slider-dots span.active { background: var(--white); }

  /* contact */
  .photo-contact { left: 0; top: 2546px; width: 620px; height: 214px; background: linear-gradient(170deg, var(--white) 10%, var(--skin) 45%, var(--towel) 85%); }
  .contact-block { left: 690px; top: 2568px; width: 290px; text-align: center; }
  .contact-block h2 { font-family: "Montserrat", sans-serif; font-weight: 600; font-size: 27px; }
  .contact-block p { margin-top: 10px; font-size: 10px; line-height: 20px; }
</style>
</head>
<body>

<header>
  <div class="abs brand"><span class="brand-mark"></span><span class="brand-name">VornaDerm</span></div>
  <div class="abs brand-tagline">The experts in permanent hair removal</div>
  <nav class="abs main-nav">
    <a style="left:478px">Home</a>
    <a style="left:563px">About</a>
    <a style="left:644px">Studios</a>
    <a style="left:741px">Booking</a>
    <a style="left:835px">News</a>
    <a style="left:903px">Careers</a>
    <a style="left:992px">Franchise</a>
  </nav>
</header>

<section class="hero">
  <div class="abs hero-photo" role="img" aria-label="Four smiling women lying side by side with legs raised"></div>
  <p class="abs front hero-lead">Lorem ipsum dolor sit amet, no duo doming audire. Ut congue posidonium mel, nominavi incorrupte mei et. Ea vim principes conceptam delicatissimi.</p>
  <div class="abs front hero-cta">Book your appointment
    <svg width="16" height="12" viewBox="0 0 16 12"><path d="M1 6h13M9 1l5 5-5 5" stroke="currentColor" stroke-width="2" fill="none"/></svg>
  </div>
</section>

<section class="about">
  <div class="abs about-panel"></div>
  <h2 class="abs section-title about-title">ABOUT</h2>

  <div class="abs feature-card card-method"></div>
  <div class="abs photo-method" role="img" aria-label="Laser device being used on a woman's hip"></div>
  <div class="abs numeral num-01">01</div>
  <div class="abs num-rule rule-01"></div>
  <div class="abs vertical-label vl-01">why permanent epilation</div>

  <div class="abs feature-text text-method">
    <h3>the method</h3>
    <div class="sub">Lorem ipsum dolor sit amet</div>
    <div class="dash"></div>
    <p>Lorem ipsum dolor sit amet, no duo doming audire. Ut congue posidonium mel, nominavi incorrupte mei et. Ea vim principes conceptam delicatissimi, eu idque nullam graecis eum. Mei idque dolores te. At sea illum nulla</p>
    <div class="more">Continue <svg width="14" height="10" viewBox="0 0 14 10"><path d="M1 5h11M8 1l4 4-4 4" stroke="currentColor" stroke-width="1.6" fill="none"/></svg></div>
  </div>

  <div class="abs feature-card card-zones"></div>
  <div class="abs photo-zones" role="img" aria-label="Woman using a handheld hair removal device on her arm"></div>

  <div class="abs feature-text text-zones">
    <h3>zones</h3>
    <div class="sub">Lorem ipsum dolor sit amet</div>
    <div class="dash"></div>
    <p>Lorem ipsum dolor sit amet, no duo doming audire. Ut congue posidonium mel, nominavi incorrupte mei et. Ea vim principes conceptam delicatissimi, eu idque nullam graecis eum. Mei idque dolores te. At sea illum nulla</p>
    <div class="more">Continue <svg width="14" height="10" viewBox="0 0 14 10"><path d="M1 5h11M8 1l4 4-4 4" stroke="currentColor" stroke-width="1.6" fill="none"/></svg></div>
  </div>

  <h2 class="abs section-title new-title">new</h2>

  <div class="abs news-band"></div>
  <div class="abs news-copy">
    <p>Lorem ipsum dolor sit amet, no duo doming audire. Ut congue posidonium mel, nominavi incorrupte mei et. Ea vim principes conceptam delicatissimi, eu idque nullam graecis eum. Mei idque dolores te. At sea illum nulla</p>
    <p>Lorem ipsum dolor sit amet, no duo doming audire. Ut congue posidonium mel, nominavi incorrupte mei et. Ea vim principes conceptam delicatissimi, eu idque nullam graecis eum. Mei idque dolores te. At sea illum nulla</p>
  </div>
  <div class="abs photo-devices" role="img" aria-label="Three professional laser hair removal machines"></div>
  <div class="abs slider-dots"><span></span><span></span><span class="active"></span></div>

  <div class="abs feature-card card-shop"></div>
  <div class="abs photo-device-pink" role="img" aria-label="White and pink home hair removal device"></div>
  <div class="abs numeral num-02">02</div>
  <div class="abs num-rule rule-02"></div>
  <div class="abs vertical-label vl-02">online shop</div>

  <div class="abs feature-text text-shop">
    <h3>online shop</h3>
    <div class="sub">Lorem ipsum dolor sit amet</div>
    <div class="dash"></div>
    <p>Lorem ipsum dolor sit amet, no duo doming audire. Ut congue posidonium mel, nominavi incorrupte mei et. Ea vim principes conceptam delicatissimi, eu idque nullam graecis eum. Mei idque dolores te. At sea illum nulla</p>
    <div class="more">More <svg width="14" height="10" viewBox="0 0 14 10"><path d="M1 5h11M8 1l4 4-4 4" stroke="currentColor" stroke-width="1.6" fill="none"/></svg></div>
  </div>
</section>

<section class="contact">
  <div class="abs photo-contact" role="img" aria-label="Woman reclining on an orange towel"></div>
  <div class="abs contact-block">
    <h2>contact</h2>
    <p>Lorem ipsum dolor sit amet, no duo doming audire. Ut congue posidonium mel, nominavi incorrupte mei et. Ea vim principes conceptam delicatissimi, eu idque nullam graecis eum. Mei idque dolores te. At sea illum nulla</p>
  </div>
</section>

</body>
</html>
```